To create a website for BRKV Accounting and Tax Services

I want to create a website that has a compelling and clean home page, social media connections, some about information, services, pricing and a spot to do simple time bookings and a contact page. I have attached a sample pricing chart, and designs of my logo, business card and letterhead. BRKV Accounting and Tax Services is a small business in beautiful Niagara on the Lake which offers bookkeeping and tax services to the local residents and businesses. I would like the winning design that use the black and blue colour scheme from my stationary and should communicate a professional business that people can trust.

Target Market(s)

local residents who need their taxes prepared as well as small business who need bookkeeping services

Industry/Entity Type

Bookkeeper

Coding

Coded - Design and coding required

Number of Pages Required

5+ page

Font styles to use
Sans Serif

Requirements
Must have
• clean home page with hero images, about section (can be on home page), separate page for services, pricing, time slot booking and contact, social media connections including facebook page, twitter, linkedin,

```html
<!DOCTYPE html>
<html lang="en">
<head>
<meta charset="utf-8">
<title>BRKV Accounting and Tax Services</title>
<link rel="stylesheet" href="https://fonts.googleapis.com/css2?family=Poppins:wght@300;400;500;600;700&family=Roboto+Slab:wght@300;400&family=Roboto:wght@300;400;500&display=swap">
<style>
:root{
  --blue:#0c83d9;
  --ink:#2f2f2f;
  --dark:#333333;
  --darker:#2a2a2a;
  --text:#555;
  --muted:#888;
  --light:#f7f7f7;
  --orange:#f26522;
  --white:#fff;
}
*{margin:0;padding:0;box-sizing:border-box}
html,body{width:1200px;height:2616px;overflow:hidden}
body{position:relative;font-family:'Roboto',sans-serif;color:var(--text);background:var(--white)}
.abs{position:absolute}
.topbar{left:0;top:0;width:1200px;height:38px;background:var(--darker);color:#ddd;font-size:11px;font-family:'Poppins',sans-serif}
.topbar .addr{left:162px;top:11px}
.topbar .links{right:162px;top:11px;display:flex;gap:16px}
.header{left:0;top:38px;width:1200px;height:93px;background:#3a3a3a}
.brand{display:flex;align-items:center;gap:10px;color:var(--white);font-family:'Poppins',sans-serif;font-weight:600;font-size:16px;letter-spacing:.5px;text-transform:uppercase;line-height:1.1}
.brand .mark{width:14px;height:14px;background:var(--blue);flex:none}
.header .brand{left:162px;top:33px}
.nav{right:162px;top:33px;display:flex;align-items:center;gap:28px;color:#eee;font-family:'Poppins',sans-serif;font-size:12px}
.nav .cta{background:var(--orange);color:var(--white);padding:7px 18px;border-radius:2px}
.hero-panel{left:0;top:131px;width:598px;height:422px;background:var(--blue)}
.hero-photo{left:598px;top:131px;width:602px;height:422px;background:linear-gradient(110deg,#e9edf1 0%,#cfd7df 45%,#9fa9b3 75%,#7f8b96 100%)}
.hero-title{left:171px;top:186px;color:var(--white);font-family:'Poppins',sans-serif;font-size:38px;font-weight:300;line-height:1.2}
.hero-title strong{display:block;font-weight:600;font-size:44px;letter-spacing:1px}
.hero-lead{left:171px;top:356px;width:400px;color:var(--white);font-family:'Roboto Slab',serif;font-size:15px;line-height:1.4}
.btn{display:flex;align-items:center;justify-content:center;font-family:'Poppins',sans-serif;font-size:12px;border-radius:2px}
.btn-light{left:171px;top:441px;width:155px;height:39px;background:var(--white);color:var(--ink)}
.btn-dark{left:342px;top:441px;width:155px;height:39px;background:#333;color:var(--white)}
.features{left:0;top:553px;width:1200px;height:279px;background:var(--light)}
.feature{width:165px;height:140px}
.feature h3{display:flex;gap:8px;width:135px;font-family:'Roboto Slab',serif;font-weight:400;font-size:14px;color:#444;line-height:1.2}
.feature h3 svg{flex:none}
.feature p{margin-top:12px;font-size:9px;line-height:1.45;color:var(--muted)}
.feature .btn{position:absolute;top:108px;left:0;width:88px;height:27px;background:var(--blue);color:var(--white);font-size:10px}
.about-photo{left:415px;top:875px;width:370px;height:112px;background:linear-gradient(90deg,#fff 0%,#dfe4ea 30%,#c8d0d9 60%,#fff 100%)}
.about-head{left:150px;top:1018px;width:900px;text-align:center;font-family:'Roboto Slab',serif;font-weight:300;font-size:24px;color:#333;line-height:1.2}
.about-text{left:250px;top:1097px;width:700px;text-align:center;font-size:8.5px;color:var(--muted);line-height:1.45}
.testimonials{left:0;top:1184px;width:1200px;height:361px;background:var(--dark)}
.t-title{left:0;top:1212px;width:1200px;text-align:center;color:var(--white);font-family:'Roboto Slab',serif;font-weight:400;font-size:22px}
.t-sub{left:0;top:1242px;width:1200px;text-align:center;color:#ccc;font-size:9px}
.quote{width:237px;height:112px;background:var(--blue);color:var(--white);text-align:center;font-family:'Roboto Slab',serif;font-size:10px;line-height:1.6;padding:14px 18px}
.quote::after{content:"";position:absolute;right:34px;bottom:-10px;border-left:10px solid transparent;border-top:10px solid var(--blue)}
.quote .q{font-size:22px;font-weight:700;line-height:1;margin-bottom:8px}
.author{width:237px;text-align:right;padding-right:56px;color:var(--white);font-family:'Roboto Slab',serif;font-size:12px}
.author small{display:block;font-size:9px;color:#ddd}
.avatar{width:44px;height:44px;border-radius:50%;background:#8aa0b4;border:2px solid #eee}
.sec-title{font-family:'Roboto Slab',serif;font-weight:300;font-size:22px;color:#333}
.service{width:200px}
.service h4{display:flex;align-items:center;gap:10px;font-family:'Roboto Slab',serif;font-weight:400;font-size:12px;color:#444}
.service p{margin-top:8px;font-size:8.5px;line-height:1.5;color:var(--muted)}
.blog{left:743px;top:1671px;width:225px;height:366px;border:1px solid #e5e5e5;background:var(--white)}
.blog .post{padding:12px 14px}
.blog h5{display:flex;align-items:center;gap:8px;font-family:'Roboto',sans-serif;font-weight:400;font-size:11px;color:#333}
.dot{width:18px;height:18px;border-radius:50%;background:#e6f2fb;border:1px solid #cfe4f4;flex:none}
.dot.grey{background:#f3f3f3;border-color:#ddd}
.blog .post p{margin:10px 0 0 24px;font-size:8.5px;line-height:1.5;color:var(--muted)}
.blog .meta{margin:12px 0 0 24px;font-size:7px;color:#999}
.blog .meta span{color:var(--blue)}
.blog .row{border-top:1px solid #e5e5e5;padding:12px 14px}
.footer{left:0;top:2115px;width:1200px;height:196px;background:var(--dark)}
.footer-brand{left:227px;top:2160px}
.contact{left:227px;top:2210px;color:var(--white);font-size:9.5px;line-height:1.6}
.contact p{margin-bottom:6px}
.newsletter{left:642px;top:2174px;color:var(--white);font-family:'Roboto Slab',serif;font-weight:400;font-size:15px}
.nl-input{left:642px;top:2210px;width:349px;height:30px;background:var(--white);font-size:9px;color:#555;padding:9px 12px}
.map{left:0;top:2311px;width:1200px;height:267px;background:linear-gradient(90deg,#e8e6e1 0%,#eceae5 35%,#d9d9d9 35%,#d9d9d9 48%,#e6e4df 48%,#eeece8 100%)}
.bottombar{left:0;top:2578px;width:1200px;height:38px;background:var(--darker);color:#ddd;font-size:10px}
.bottombar .copy{left:168px;top:12px}
.social{right:168px;top:13px;display:flex;gap:18px}
.social i{display:block;width:10px;height:10px;border-radius:50%;background:#ccc}
</style>
</head>
<body>

<div class="abs topbar">
  <span class="abs addr">88 Queen Street, Harborview, ON K0A 3B0</span>
  <div class="abs links"><span>Cart £0.00</span><span>|</span><span>Register</span><span>|</span><span>Client login</span></div>
</div>

<header class="abs header">
  <div class="abs brand"><span class="mark"></span><span>BRKV Accounting and Tax<br>Services</span></div>
  <nav class="abs nav"><span>Home</span><span>About</span><span>Services</span><span>Pricing</span><span>Blog</span><span class="cta">Appointment</span><span>Contact</span></nav>
</header>

<section>
  <div class="abs hero-panel"></div>
  <div class="abs hero-photo" role="img" aria-label="Smiling businessman in a grey suit with colleagues at a meeting table behind him"></div>
  <h1 class="abs hero-title">Professional<strong>TAX / BUSINESS</strong>Service</h1>
  <p class="abs hero-lead">Our courses are built in partnerships with technology leaders and are relevant to industry needs.</p>
  <a class="abs btn btn-light">Free Consultation</a>
  <a class="abs btn btn-dark">More About Us</a>
</section>

<section class="abs features">
  <div class="abs feature" style="left:237px;top:83px">
    <h3><svg width="22" height="22" viewBox="0 0 22 22"><circle cx="11" cy="7" r="5" fill="#d9412b"/><rect x="4" y="13" width="14" height="8" rx="3" fill="#444"/></svg>Check Status Of Your Return</h3>
    <p>We are ready to provide you with up-to-date refund information online, by phone, or during personal meeting</p>
    <a class="btn">Read More</a>
  </div>
  <div class="abs feature" style="left:426px;top:83px">
    <h3><svg width="22" height="22" viewBox="0 0 22 22"><rect x="4" y="1" width="14" height="20" rx="2" fill="#555"/><rect x="6" y="3" width="10" height="5" fill="#9fd3f5"/><rect x="6" y="11" width="10" height="8" fill="#ccc"/></svg>Withholding Calculator</h3>
    <p>If you are an employee, you can apply for help to decide whether you need to give your employer a new form W-4</p>
    <a class="btn">Read More</a>
  </div>
  <div class="abs feature" style="left:616px;top:83px">
    <h3><svg width="22" height="22" viewBox="0 0 22 22"><path d="M1 11 11 2l10 9z" fill="#d9412b"/><rect x="4" y="11" width="14" height="10" fill="#e7a33c"/><rect x="9" y="14" width="4" height="7" fill="#fff"/></svg>Property Taxes</h3>
    <p>If you need help paying property tax, wish to apply for a property tax refund etc., our tax specialists are here for you</p>
    <a class="btn">Read More</a>
  </div>
  <div class="abs feature" style="left:804px;top:83px">
    <h3><svg width="22" height="22" viewBox="0 0 22 22"><path d="M1 7 11 1l10 6z" fill="#888"/><rect x="3" y="8" width="3" height="10" fill="#999"/><rect x="9.5" y="8" width="3" height="10" fill="#999"/><rect x="16" y="8" width="3" height="10" fill="#999"/><rect x="1" y="18" width="20" height="3" fill="#888"/></svg>Own a Business?</h3>
    <p>As a business owner, you must know all tax pitfalls, that's why our business planning department is working for you</p>
    <a class="btn">Read More</a>
  </div>
</section>

<section>
  <div class="abs about-photo" role="img" aria-label="Two business colleagues walking through a bright glass office"></div>
  <h2 class="abs about-head">We believe that selecting the right financial services firm is<br>paramount to the financial success of any person or organization.</h2>
  <p class="abs about-text">Our office believes in building relationships with our clients, and we view these relationships as partnerships. Our service is founded on commitment, dedication and professionalism of our people. We strive to serve our clients by adhering to our own standard of excellence. Our business philosophy is to partner with our clients to provide them with the highest quality of services by implementing practices of nothing less than excellence as a firm standard.</p>
</section>

<section class="abs testimonials"></section>
<h2 class="abs t-title">Testimonial</h2>
<p class="abs t-sub">what client says</p>

<div class="abs quote" style="left:204px;top:1304px"><div class="q">&ldquo;</div>The team has provided tax help to me and my company and my company form an early stage of our development</div>
<div class="abs quote" style="left:481px;top:1304px"><div class="q">&ldquo;</div>The team has provided tax help to me and my company and my company form an early stage of our development</div>
<div class="abs quote" style="left:757px;top:1304px"><div class="q">&ldquo;</div>The team has provided tax help to me and my company and my company form an early stage of our development</div>

<div class="abs author" style="left:204px;top:1439px">Dana Whitfield<small>It Consultant</small></div>
<div class="abs avatar" style="left:391px;top:1434px" role="img" aria-label="Client portrait"></div>
<div class="abs author" style="left:481px;top:1439px">Dana Whitfield<small>It Consultant</small></div>
<div class="abs avatar" style="left:668px;top:1434px" role="img" aria-label="Client portrait"></div>
<div class="abs author" style="left:757px;top:1439px">Dana Whitfield<small>It Consultant</small></div>
<div class="abs avatar" style="left:944px;top:1434px" role="img" aria-label="Client portrait"></div>

<h2 class="abs sec-title" style="left:244px;top:1610px">Our Services</h2>

<div class="abs service" style="left:244px;top:1675px">
  <h4><svg width="16" height="16" viewBox="0 0 16 16"><rect x="1" y="1" width="14" height="14" rx="2" fill="#0c83d9"/><rect x="3" y="3" width="10" height="3" fill="#fff"/></svg>Audit &amp; Assurance</h4>
  <p>Delivering premium quality and comprehensive audit and assurance services is one of our highest priorities</p>
</div>
<div class="abs service" style="left:467px;top:1675px">
  <h4><svg width="16" height="16" viewBox="0 0 16 16"><rect x="2" y="1" width="12" height="14" rx="2" fill="#0c83d9"/><rect x="4" y="3" width="8" height="3" fill="#fff"/></svg>Tax Advisory Services</h4>
  <p>We are ready to provide you with up-to-date tax information online, by phone, or during personal meeting</p>
</div>
<div class="abs service" style="left:244px;top:1764px">
  <h4><svg width="16" height="16" viewBox="0 0 16 16"><path d="M8 1a7 7 0 1 0 7 7H8z" fill="#0c83d9"/><path d="M9.5 0v6.5H16A7 7 0 0 0 9.5 0z" fill="#0c83d9"/></svg>Business Services</h4>
  <p>As a business owner, you must know all tax pitfalls, that's why our business planning department is working for you</p>
</div>
<div class="abs service" style="left:467px;top:1764px">
  <h4><svg width="16" height="16" viewBox="0 0 16 16"><rect x="1" y="3" width="14" height="12" rx="1" fill="#0c83d9"/><rect x="3" y="7" width="10" height="6" fill="#fff"/><rect x="4" y="1" width="2" height="4" fill="#0c83d9"/><rect x="10" y="1" width="2" height="4" fill="#0c83d9"/></svg>Year-End Tax Planning</h4>
  <p>Using proper tax planning, our professionals will teach you how to pay less tax and receive optimal returns</p>
</div>
<div class="abs service" style="left:244px;top:1853px">
  <h4><svg width="16" height="16" viewBox="0 0 16 16"><path d="M2 14C2 6 8 2 15 1c-1 7-5 13-13 13z" fill="#0c83d9"/></svg>IT Control Solutions</h4>
  <p>We'll find the solutions you need to boost your financial life today and make the most of your cash resources</p>
</div>
<div class="abs service" style="left:467px;top:1853px">
  <h4><svg width="16" height="16" viewBox="0 0 16 16"><circle cx="8" cy="8" r="6" fill="none" stroke="#0c83d9" stroke-width="3" stroke-dasharray="3 2"/><circle cx="8" cy="8" r="3" fill="#0c83d9"/></svg>Financial Planning</h4>
  <p>We will work through the process to identify your needs, goals and strategy, and put your plan into action</p>
</div>

<h2 class="abs sec-title" style="left:743px;top:1610px">From the Blog</h2>
<div class="abs blog">
  <div class="post">
    <h5><span class="dot"></span>Top Tax Issues</h5>
    <p>Lorem ipsum dolor sit amet, consectetur adipiscing elit. In aliquam ante nec magna pharetra feugiat. Phasellus et lorem ac mauris sagittis feugiat. Fusce euismod ac urna eu blandit. Sed eget blandit diam. Praesent quis est id ligula viverra pulvinar eu consectetur neque. Nam bibendum porttitor velit quis gravida. Curabitur dui tellus, feugiat at pharetra quis.</p>
    <div class="meta">Posted by brkvstaff &nbsp;/&nbsp; <span>Views 1275</span></div>
  </div>
  <div class="row"><h5><span class="dot grey"></span>New Tax Pitfalls to Avoid</h5></div>
  <div class="row"><h5><span class="dot grey"></span>Pros and Cons of Muni Bonds</h5></div>
  <div class="row"><h5><span class="dot grey"></span>7 Most Common Tax Mistakes</h5></div>
</div>

<footer class="abs footer"></footer>
<div class="abs brand footer-brand"><span class="mark"></span><span>BRKV Accounting and Tax<br>Services</span></div>
<div class="abs contact">
  <p>905-555-0182</p>
  <p>hello@brkvtax.example</p>
  <p>210 Kingsbridge Road, Suite 14<br>P.O. Box 417 Lakeview,<br>ON K0A 2M0</p>
</div>
<h3 class="abs newsletter">Subscribe Newsletter</h3>
<div class="abs nl-input">your email id
  <svg class="abs" style="right:12px;top:11px" width="10" height="8" viewBox="0 0 10 8"><path d="M0 4h8M5 1l3 3-3 3" stroke="#333" stroke-width="1.4" fill="none"/></svg>
</div>

<div class="abs map" role="img" aria-label="Street map showing the office location"></div>

<div class="abs bottombar">
  <span class="abs copy">© 2019 All Rights Reserved.</span>
  <div class="abs social"><i></i><i></i><i></i><i></i><i></i><i></i></div>
</div>

</body>
</html>
```